Business Card Design

I am starting my therapy private practice. I will be an in home therapist, so I go into family's homes instead of using an office to do family/marriage therapy. Therefore, I do not have an office address. I am looking for something in the black, red, gray, and blue color scheme that appeals to both families, couples and teenagers.

Industry/Entity Type

Business

Contact Information for Business Card

Lena Brightwell, MS, Hearthway Intern
Marriage and Family Therapy
In Home Therapist
617-482-5190
Lena@LenaBrightwell-example.com

```html
<!DOCTYPE html>
<html lang="en">
<head>
<meta charset="utf-8">
<title>Business Card – Lena Brightwell</title>
<link rel="stylesheet" href="https://fonts.googleapis.com/css2?family=Open+Sans:wght@400;600;700;800&display=swap">
<style>
  :root {
    --backdrop: #e6e6e6;
    --card: #f7f7f7;
    --red: #e01f26;
    --ink: #2a2a2a;
    --grey: #6e6e6e;
    --blue: #2a9de0;
    --black: #1e1e1e;
  }
  * { margin: 0; padding: 0; box-sizing: border-box; }
  html, body {
    width: 1200px;
    height: 1200px;
    overflow: hidden;
    background: var(--backdrop);
    font-family: "Open Sans", sans-serif;
  }
  .card {
    position: absolute;
    left: 100px;
    top: 314px;
    width: 1000px;
    height: 572px;
    background: var(--card);
    box-shadow: 0 10px 30px rgba(0,0,0,0.12);
    overflow: hidden;
  }
  .brand {
    position: absolute;
    left: 90px;
    top: 96px;
    display: flex;
    align-items: center;
    gap: 18px;
  }
  .brand-dot {
    width: 46px;
    height: 46px;
    border-radius: 50%;
    background: var(--red);
  }
  .brand-name {
    font-size: 64px;
    font-weight: 800;
    color: var(--red);
    letter-spacing: 1px;
    line-height: 1;
  }
  .tagline {
    position: absolute;
    left: 90px;
    top: 186px;
    font-size: 30px;
    font-weight: 700;
    color: var(--ink);
  }
  .person {
    position: absolute;
    left: 90px;
    top: 250px;
  }
  .person-name {
    font-size: 32px;
    font-weight: 700;
    color: var(--red);
    line-height: 1.2;
  }
  .person-role {
    font-size: 24px;
    font-weight: 400;
    color: var(--grey);
  }
  .contact {
    position: absolute;
    left: 500px;
    top: 370px;
    list-style: none;
  }
  .contact-item {
    display: flex;
    align-items: center;
    gap: 12px;
    font-size: 24px;
    color: var(--ink);
    line-height: 1.5;
  }
  .contact-icon { width: 22px; height: 22px; flex: none; }
  .band {
    position: absolute;
    left: 0;
    bottom: 0;
    width: 100%;
    height: 40px;
    display: flex;
  }
  .band-blue { width: 42%; background: var(--blue); }
  .band-black { flex: 1; background: var(--black); }
</style>
</head>
<body>
  <article class="card">
    <div class="brand">
      <span class="brand-dot"></span>
      <span class="brand-name">Hearthway</span>
    </div>
    <p class="tagline">Intern Marriage &amp; Family Therapy</p>
    <div class="person">
      <p class="person-name">Lena Brightwell, MS</p>
      <p class="person-role">Home Therapist</p>
    </div>
    <ul class="contact">
      <li class="contact-item">
        <svg class="contact-icon" viewBox="0 0 24 24" aria-hidden="true">
          <circle cx="12" cy="12" r="12" fill="#3a3a3a"/>
          <path d="M8.5 6.5c.6-.5 1.3-.4 1.7.2l1 1.6c.3.5.2 1.1-.2 1.5l-.7.6c.6 1.3 1.5 2.3 2.8 3l.6-.7c.4-.4 1-.5 1.5-.2l1.6 1c.6.4.7 1.1.2 1.7-1 1.2-2.5 1.5-4 .7-2.3-1.2-4-3-5.1-5.2-.8-1.6-.5-3.1.6-4.2z" fill="#fff"/>
        </svg>
        (617) 482-5190
      </li>
      <li class="contact-item">
        <svg class="contact-icon" viewBox="0 0 24 24" aria-hidden="true">
          <circle cx="12" cy="12" r="12" fill="#3a3a3a"/>
          <rect x="6" y="8" width="12" height="8" rx="1" fill="#fff"/>
          <path d="M6.5 8.5l5.5 4 5.5-4" fill="none" stroke="#3a3a3a" stroke-width="1.2"/>
        </svg>
        Lena@LenaBrightwell-example.com
      </li>
    </ul>
    <div class="band">
      <span class="band-blue"></span>
      <span class="band-black"></span>
    </div>
  </article>
</body>
</html>
```